Website Redesign for a faith-based, not-for-profit health and human services organization

New website design for the Harbor Faith Outreach Hall.
- Current site: www.hfohlp.org -
We are looking for a nice clean, simple, friendly-yet-elegant website layout.
Colors are #f5eed5 (cream), #FFFFFF (white), and all logo colors.
Design a layout for home page
Design a layout for general layouts
-layout only no html needed (preferably a high res PSD file format) -
Main menu should be along top with side navigation for submenu, no side menu on home page.
Also would be open to seeing some updated colors on the logo design, currently the colors are slightly outdated. The Vine of Morning quilt design fits the organization’s mission and the rural farming / Amish-Mennonite-Brethren community around us.

ADDITIONAL PAGES AND MENU STRUCTURE ON NEW SITE

- How to Help
... Volunteer
... Donate Time
... Donate Money
... Donate Supplies
... Current Needs

- Programs

- News & Events
... Upcoming Events
... Upcoming Fundraisers
... Newsletter

- Our Partners

- About Us
... Overview
... Mission
... Staff Directory
... Board of Directors
... Annual Reports

- Contact

Our annual special event is Gather at the Hearth and should be integrated into the home page - see attached logos and banner

Websites with elements we like (from organizations doing similar work), each for a different reason....

1. http://www.kinroutesnet.org
Good design, color, clarity on this site. Multi-dimensional, photos...easy interaction, etc.

2. http://endemptyplates.org
Quite simple, nothing fancy, but some good basic stuff here, and pretty easy to navigate...

3. http://www.folkhubvx.org
Intrigued by the bulletin board design and the way they have their programs broken down to show impact, needs, etc. It has a lot of good information, but is really too verbose, some of the print is too small, etc. Not perfect, but some interesting design elements.

4. http://sharedlarder.org
Site is boring and not very well designed, but it has some of the features that we would like to see at the top, donations, partners, etc.

5. http://www.zenithmealshelf.org
Too many listings on the sidebar - needs to be cleaner & simpler, but a lot of good information and we like the way they show volunteer photos on the Our Helpers Shine page...

About
Harbor Faith Outreach Hall ("HFOH" or “the Center”) is a faith-based non-for-profit health and human services organization that exists as an outreach of and for the Lo-Bray Community School District.
Tagline: Kindness at Work (we work to serve the needs of the ‘least of these’ with compassion).

Mission
Our mission is to see lives transformed and the community enhanced by encouraging the oppressed, defending the cause of the weak and maintaining the rights of the poor - bringing together the resources of a caring community as a demonstration of the good news of Christ.

Company Overview
Harbor Faith Outreach Hall works closely with the community in which it serves. A tremendous value is placed upon the partnerships that have formed with caring people within the community and with organizations that share the goal of bringing together resources to help those who need it most. Individuals, volunteers, churches, corporations, foundations, and government sources all pull together to help make our mission possible.

Since 1996 the Harbor Faith Outreach Hall has collaboratively worked to see our community enhanced, adapting programs and services to meet the changing needs of the community.

Target Market(s)

people needing assistance in local community

Industry/Entity Type

Government

Requirements
Must have
• Good social button integration
Should not have
• No Find Us page like old website it is not needed

```html
<!DOCTYPE html>
<html lang="en">
<head>
<meta charset="utf-8">
<title>Harbor Faith Outreach Hall</title>
<link href="https://fonts.googleapis.com/css2?family=Dosis:wght@400;500;600&display=swap" rel="stylesheet">
<style>
:root{
  --orange:#c87a12;
  --green-dark:#173d26;
  --green:#1f5130;
  --mint:#8fc2b3;
  --mint-dark:#79ab9e;
  --slate:#4f6f63;
  --wine:#8e1f36;
  --footer:#2d4a3d;
  --charcoal:#2a2a2a;
  --bar:#1f2822;
  --cream:#f5eed5;
  --white:#ffffff;
  --text:#1f2e27;
  --accent:#e09a2a;
}
*{box-sizing:border-box;margin:0;padding:0}
html,body{width:889px;height:1200px;overflow:hidden}
body{background:var(--orange);font-family:"Dosis",sans-serif;color:var(--text);position:relative}
.abs{position:absolute}
.topbar{left:0;top:0;width:889px;height:61px;background:linear-gradient(#1e5131,#0f3019)}
.brand{left:75px;top:0;width:176px;height:117px;background:var(--white);box-shadow:0 2px 6px rgba(0,0,0,.3);display:flex;align-items:center;gap:8px;padding:0 10px}
.brand-mark{width:22px;height:22px;background:var(--wine);flex:none}
.brand-name{color:var(--green);font-size:16px;font-weight:500;line-height:1.05}
.nav{left:251px;top:0;height:61px;display:flex}
.nav a{display:flex;align-items:center;height:61px;padding:0 8.5px;color:var(--white);text-decoration:none;font-size:13.5px;white-space:nowrap;border-right:1px solid rgba(255,255,255,.12)}
.nav a.active{background:linear-gradient(#2d7545,#1d5230);border-bottom:4px solid #3a9a55}
.hero{left:75px;top:61px;width:740px;height:296px;background:linear-gradient(160deg,#8a6a5a 0%,#c9c4bd 35%,#e6e4e0 60%,#6d6150 100%);overflow:hidden}
.hero-cap{position:absolute;right:8px;bottom:12px;color:var(--white);font-size:18px;white-space:nowrap;text-shadow:0 1px 3px rgba(0,0,0,.7)}
.arrow{top:178px;width:30px;height:64px;background:var(--white);display:flex;align-items:center;justify-content:center}
.arrow.left{left:75px;border-radius:0 4px 4px 0}
.arrow.right{left:785px;border-radius:4px 0 0 4px}
.social{left:851px;top:165px;width:38px;height:70px;background:var(--green-dark);border-radius:5px 0 0 5px;display:flex;flex-direction:column;align-items:center;justify-content:space-evenly}
.social span{width:20px;height:20px;border-radius:50%;background:#3f8a5c}
.subbar{left:75px;top:357px;width:740px;height:40px;background:var(--bar);display:flex;align-items:center;color:var(--white);font-size:11.5px;padding-left:14px;white-space:nowrap}
.field{height:20px;background:#c9c9c9;border:1px solid #888}
.btn-tan{height:20px;background:#e7d9ae;color:#222;font-size:11.5px;padding:0 6px;display:flex;align-items:center;gap:4px}
.donate{background:#2e7a9a;color:var(--white);height:22px;padding:0 8px;display:flex;align-items:center;gap:5px;font-size:11.5px}
.divider{width:1px;height:40px;background:#444;margin:0 12px}
.community{left:75px;top:397px;width:740px;height:222px;background:linear-gradient(#1d5230,#173f26)}
.community h2{text-align:center;color:var(--cream);font-weight:500;font-size:19px;padding-top:12px}
.thumb{top:463px;width:171px;height:113px;border:2px solid #d9d9d9}
.scroll-track{left:89px;top:593px;width:714px;height:2px;background:#4a7a58}
.scroll-knob{left:103px;top:585px;width:56px;height:18px;background:#2f7a46;border-radius:4px}
.about{left:75px;top:619px;width:521px;height:250px;background:var(--mint);padding:16px 20px}
.about h1{font-size:21px;font-weight:500;color:var(--text)}
.about h1 em{font-style:normal;color:var(--accent)}
.about p{font-size:10.5px;line-height:1.45;margin-top:12px;color:#1b2a24}
.btn-more{background:var(--slate);color:#e7efe9;font-size:12px;padding:4px 12px;border-radius:3px;display:inline-block}
.events{left:596px;top:619px;width:220px;height:250px;background:var(--mint-dark);padding:16px 20px}
.events h2{font-size:20px;font-weight:500;color:var(--text)}
.event{display:flex;gap:12px;margin-top:14px}
.date{width:36px;height:33px;background:#3f5a50;color:var(--white);font-size:8.5px;text-align:center;line-height:1.3;padding-top:3px;flex:none}
.event p{font-size:9.5px;line-height:1.3;color:#1b2a24}
.partners-tab{left:87px;top:880px;width:133px;height:27px;background:var(--footer);color:var(--cream);font-size:15px;display:flex;align-items:center;justify-content:center}
.partners{left:75px;top:907px;width:440px;height:140px;background:var(--wine)}
.p-arrow{top:952px;width:24px;height:46px;background:var(--orange);display:flex;align-items:center;justify-content:center}
.badge{top:940px;width:180px;height:68px;background:var(--white);border:2px solid #222}
.badge.dark{background:#3a3a3a;border-color:#ddd}
.hearth{left:525px;top:893px;width:291px;height:154px;background:var(--slate);padding:10px 14px;color:#c4d4cb;font-size:10.5px;line-height:1.35;white-space:nowrap}
.hearth-name{left:620px;top:1002px;display:flex;align-items:center;gap:8px;color:var(--cream);font-size:17px;font-weight:500;white-space:nowrap}
.hearth-name span{width:14px;height:14px;background:var(--orange)}
.footer{left:0;top:1060px;width:889px;height:113px;background:var(--footer)}
.f-brand{left:98px;top:1075px;display:flex;align-items:center;gap:8px}
.f-brand .brand-mark{background:#6c8a7c}
.f-brand .brand-name{color:#b9c8bf;font-size:16px;width:100px}
.f-nav{left:296px;top:1086px;display:flex;gap:18px}
.f-nav a{color:var(--white);text-decoration:none;font-size:12.5px;white-space:nowrap}
.f-line{left:292px;top:1113px;width:500px;height:1px;background:#48665a}
.f-info{left:292px;top:1120px;width:500px;text-align:center;color:#d9e2dc;font-size:12.5px;line-height:1.4}
.copy{left:0;top:1173px;width:889px;height:27px;background:var(--charcoal);color:#aaa;font-size:11.5px;display:flex;align-items:center;justify-content:center}
</style>
</head>
<body>
<div class="abs topbar"></div>
<nav class="abs nav">
  <a class="active" href="#">HOME</a><a href="#">EVENTS</a><a href="#">HOW TO HELP</a><a href="#">PROGRAMES</a><a href="#">OUR PARTERNERS</a><a href="#">ABOUT US</a><a href="#">CONTACT</a>
</nav>

<div class="abs hero" role="img" aria-label="Group photo of volunteers in matching white t-shirts">
  <div class="hero-cap">we work to serve the needs of the ‘least of these’ with compassion</div>
</div>
<div class="abs brand"><span class="brand-mark"></span><span class="brand-name">Harbor Faith Outreach Hall</span></div>
<div class="abs arrow left"><svg width="14" height="16"><path d="M11 2 4 8l7 6" fill="none" stroke="#d9531e" stroke-width="3"/></svg></div>
<div class="abs arrow right"><svg width="14" height="16"><path d="M3 2l7 6-7 6" fill="none" stroke="#d9531e" stroke-width="3"/></svg></div>
<div class="abs social"><span></span><span></span></div>

<div class="abs subbar">
  Subscribe to newsletter for updates
  <span class="field" style="width:146px;margin-left:8px"></span>
  <span class="btn-tan" style="margin-left:4px">SUBSCRIBE</span>
  <span class="divider" style="margin-left:16px"></span>
  <span class="donate">DONATE NOW <svg width="8" height="10"><path d="M2 1l4 4-4 4" fill="none" stroke="#fff" stroke-width="2"/></svg></span>
  <span class="divider"></span>
  <span class="field" style="width:146px"></span>
  <span class="btn-tan" style="margin-left:4px">SEARCH <svg width="11" height="11"><circle cx="4.5" cy="4.5" r="3.2" fill="none" stroke="#222" stroke-width="1.5"/><path d="M7 7l3 3" stroke="#222" stroke-width="1.8"/></svg></span>
</div>

<section class="abs community">
  <h2>Harbor Faith Outreach Hall works closely with the community in which it serves</h2>
</section>
<div class="abs thumb" style="left:89px;background:linear-gradient(#b9a08a,#e5ddd2)" role="img" aria-label="Volunteers serving food at a table"></div>
<div class="abs thumb" style="left:271px;background:linear-gradient(#d9b43a,#3a3a3a)" role="img" aria-label="School bus food drive with children"></div>
<div class="abs thumb" style="left:452px;background:linear-gradient(#c8c4bc,#8e7a6a)" role="img" aria-label="Volunteers gathered indoors"></div>
<div class="abs thumb" style="left:632px;background:linear-gradient(#d5d8dc,#9a8f84)" role="img" aria-label="Volunteers outside a delivery truck"></div>
<div class="abs scroll-track"></div>
<div class="abs scroll-knob"></div>

<section class="abs about">
  <h1>Building a Better Community - for <em>16 years!</em></h1>
  <p>Harbor Faith Outreach Hall works closely with the community in which it serves. A tremendous amount of value is placed upon the partnerships that have formed with caring people within the community and organizations that share the goal of bringing together resources to help those who need it most. Individuals, volunteers, churches, corporations, foundations, and government sources all pull together to help make our mission possible. Since 1996 Harbor Faith Outreach Hall has collaboratively worked to see our community enhanced.</p>
  <p>Our mission is to see lives transformed and the community enhanced by encouraging the oppressed, defending the cause of the weak and maintaining the rights of the poor by bringing together the resources of a caring community as a demonstration of the good news of Christ..........................</p>
  <p style="margin-top:14px"><span class="btn-more">Read More</span></p>
</section>
<aside class="abs events">
  <h2>Upcoming Events</h2>
  <div class="event"><div class="date">9<br>MARCH</div><p>Soup Supper Fundraiser, Soup Supper Fundraiser</p></div>
  <div class="event"><div class="date">9<br>MARCH</div><p>Soup Supper Fundraiser, Soup Supper Fundraiser</p></div>
  <div class="event"><div class="date">9<br>MARCH</div><p>Soup Supper Fundraiser, Soup Supper Fundraiser</p></div>
  <p style="text-align:right;margin-top:18px"><span class="btn-more">More events</span></p>
</aside>

<div class="abs partners"></div>
<div class="abs partners-tab">OUR PARTNERS</div>
<div class="abs p-arrow" style="left:79px"><svg width="10" height="14"><path d="M8 2 3 7l5 5" fill="none" stroke="#fff" stroke-width="2.5"/></svg></div>
<div class="abs badge" style="left:118px"></div>
<div class="abs badge dark" style="left:310px"></div>
<div class="abs p-arrow" style="left:486px"><svg width="10" height="14"><path d="M2 2l5 5-5 5" fill="none" stroke="#fff" stroke-width="2.5"/></svg></div>

<div class="abs hearth">THANK YOU TO OUR PARTNERS AND EVERYONE WHO HELPED<br>MAKE OUR FIRST FARM-TO-TABLE<br>EVENT A SUCCESS!</div>
<div class="abs hearth-name"><span></span>Gather at the Hearth</div>

<footer class="abs footer"></footer>
<div class="abs f-brand"><span class="brand-mark"></span><span class="brand-name">Harbor Faith Outreach Hall</span></div>
<nav class="abs f-nav"><a href="#">HOME</a><a href="#">EVENTS</a><a href="#">HOW TO HELP</a><a href="#">PROGRAMES</a><a href="#">OUR PARTERNERS</a><a href="#">ABOUT US</a><a href="#">CONTACT</a></nav>
<div class="abs f-line"></div>
<div class="abs f-info">Harbor Faith Outreach Hall&nbsp;&nbsp; 48 North Alder Lane&nbsp;&nbsp; Brookvale&nbsp;&nbsp; IN&nbsp;&nbsp; 40000<br>Ph.: 555.010.2149&nbsp; Fax 555.010.5337</div>
<div class="abs copy">© 2013 Harbor Faith Outreach Hall. All Rights Reserved</div>
</body>
</html>
```